Corvane Medical new year card

Hi,
I would like a New Year greetings card to send to my customers.

If you need to look at our logo : www.corvanemedical.com

If you want to play with images of our device, see
trelvacare.ca

The goal is to have a card to wish a happy new year and we look forward collaborating with them in the new year.

```html
<!DOCTYPE html>
<html lang="en">
<head>
<meta charset="utf-8">
<title>Corvane Medical — Happy New Year 2022</title>
<link rel="stylesheet" href="https://fonts.googleapis.com/css2?family=Montserrat:wght@400;600;700&display=swap">
<style>
  :root {
    --page: #ffffff;
    --card-centre: #fdf8ee;
    --card-mid: #f1dfbd;
    --card-edge: #c8923c;
    --brand-grey: #5f5f62;
    --brand-accent: #e0632a;
    --greeting-red: #8c2a1c;
    --glow-warm: rgba(238, 190, 95, 0.55);
    --device-tone: rgba(210, 205, 200, 0.55);
    --numeral-cream-top: #fffaf0;
    --numeral-cream-bottom: #e8d7b8;
    --numeral-gold-top: #f7c640;
    --numeral-gold-bottom: #b87812;
    --numeral-edge: #a8782c;
  }
  * { margin: 0; padding: 0; box-sizing: border-box; }
  html, body {
    width: 1200px;
    height: 1063px;
    overflow: hidden;
    background: var(--page);
  }
  .canvas {
    position: relative;
    width: 1200px;
    height: 1063px;
  }
  .greeting-card {
    position: absolute;
    left: 221px;
    top: 211px;
    width: 746px;
    height: 636px;
    background: radial-gradient(ellipse 75% 80% at 48% 50%, var(--card-centre) 0%, var(--card-mid) 58%, var(--card-edge) 100%);
    overflow: hidden;
  }
  .brand {
    position: absolute;
    left: 0;
    right: 0;
    top: 64px;
    display: flex;
    justify-content: center;
    align-items: center;
    gap: 10px;
    font-family: "Montserrat", sans-serif;
    font-weight: 600;
    font-size: 26px;
    color: var(--brand-grey);
    letter-spacing: -0.01em;
  }
  .brand-square {
    width: 18px;
    height: 18px;
    background: var(--brand-accent);
  }
  .celebration-art {
    position: absolute;
    left: 130px;
    top: 160px;
    width: 480px;
    height: 380px;
    border-radius: 50%;
    background:
      radial-gradient(ellipse 42% 16% at 42% 78%, var(--device-tone) 0%, rgba(210, 205, 200, 0) 100%),
      radial-gradient(ellipse 50% 50% at 56% 42%, var(--glow-warm) 0%, rgba(238, 190, 95, 0) 100%);
  }
  .year {
    position: absolute;
    inset: 0;
    font-family: "Montserrat", sans-serif;
    font-weight: 700;
    font-size: 232px;
    line-height: 1;
  }
  .year-digit {
    position: absolute;
    background: linear-gradient(180deg, var(--numeral-cream-top) 0%, var(--numeral-cream-bottom) 100%);
    -webkit-background-clip: text;
    background-clip: text;
    color: transparent;
    filter: drop-shadow(2px 3px 0 var(--numeral-edge)) drop-shadow(0 6px 10px rgba(150, 100, 30, 0.35));
  }
  .year-digit--gold {
    background: linear-gradient(180deg, var(--numeral-gold-top) 0%, var(--numeral-gold-bottom) 100%);
    -webkit-background-clip: text;
    background-clip: text;
  }
  .year-digit--1 { left: 196px; top: 206px; }
  .year-digit--2 { left: 280px; top: 182px; }
  .year-digit--3 { left: 362px; top: 142px; }
  .year-digit--4 { left: 440px; top: 188px; }
  .greeting {
    position: absolute;
    left: 0;
    right: 0;
    top: 550px;
    display: flex;
    justify-content: center;
    align-items: center;
    gap: 11px;
    font-family: "Montserrat", sans-serif;
    font-weight: 400;
    font-size: 15px;
    letter-spacing: 0.78em;
    color: var(--greeting-red);
  }
  .greeting-dot {
    width: 4px;
    height: 4px;
    border-radius: 50%;
    background: var(--greeting-red);
    flex: none;
  }
  .greeting-word { margin-right: -0.78em; }
</style>
</head>
<body>
  <div class="canvas">
    <section class="greeting-card">
      <div class="brand">
        <span class="brand-square"></span>
        <span class="brand-name">Corvane Medical</span>
      </div>

      <div class="celebration-art" role="img" aria-label="Gold ribbons and scattered confetti around the numerals, with the Corvane Medical headset device and its cabled mouthpiece resting in front"></div>

      <h1 class="year" aria-label="2022">
        <span class="year-digit year-digit--1">2</span>
        <span class="year-digit year-digit--2">0</span>
        <span class="year-digit year-digit--gold year-digit--3">2</span>
        <span class="year-digit year-digit--4">2</span>
      </h1>

      <p class="greeting">
        <span class="greeting-dot"></span>
        <span class="greeting-word">HAPPY</span>
        <span class="greeting-dot"></span>
        <span class="greeting-word">NEW</span>
        <span class="greeting-dot"></span>
        <span class="greeting-word">YEAR</span>
        <span class="greeting-dot"></span>
      </p>
    </section>
  </div>
</body>
</html>
```